Kindle Your Patrons Book Cover

A book main title will be, "Kindle Your Patrons"
The subtext will be, "Go to market with a story that sizzles"
Would like it to blend with my web site brand. You can find it here: www.kindleyourpatrons.example

Audience is business and revenue leaders for small, medium and large businesses. They have a new solution, or want to enter a new market, and they need to "kindle their patrons" meaning getting the buyers to want to change enough to overcome their status quo bias. They need a story that sizzles to do this.

```html
<!DOCTYPE html>
<html lang="en">
<head>
<meta charset="utf-8">
<title>Kindle Your Patrons — Book Cover</title>
<link rel="stylesheet" href="https://fonts.googleapis.com/css2?family=Montserrat:ital,wght@0,500;0,700;0,800;1,300&display=swap">
<style>
  :root {
    --backdrop: #626262;
    --paper: #ffffff;
    --title-teal: #5bbfbf;
    --field-teal: #66d8d6;
    --field-teal-deep: #5ccdcb;
    --ink-gray: #5a5a5a;
    --sizzle-red: #e0352b;
    --mark-white: #f4fbfb;
  }
  * { margin: 0; padding: 0; box-sizing: border-box; }
  html, body {
    width: 924px;
    height: 1200px;
    overflow: hidden;
    background: var(--backdrop);
  }
  .cover {
    position: absolute;
    left: 150px;
    top: 126px;
    width: 624px;
    height: 936px;
    background: var(--paper);
    border: 1px solid #1a1a1a;
    overflow: hidden;
    font-family: "Montserrat", Arial, sans-serif;
  }
  .title {
    position: absolute;
    left: 56px;
    top: 36px;
    color: var(--title-teal);
    font-size: 112px;
    line-height: 93px;
    letter-spacing: -0.05em;
  }
  .title span { display: block; }
  .title__strong { font-weight: 800; }
  .title__light { font-weight: 300; font-style: italic; letter-spacing: -0.02em; }
  .subtitle {
    position: absolute;
    left: 58px;
    top: 345px;
    font-size: 20px;
    font-weight: 500;
    color: var(--ink-gray);
    letter-spacing: -0.01em;
  }
  .subtitle__accent { color: var(--sizzle-red); font-weight: 700; }
  .photo-field {
    position: absolute;
    left: 0;
    top: 432px;
    width: 100%;
    height: 504px;
    background: radial-gradient(circle at 70% 40%, var(--field-teal) 0%, var(--field-teal-deep) 100%);
  }
  .site {
    position: absolute;
    right: 50px;
    bottom: 32px;
    display: flex;
    align-items: center;
    gap: 10px;
    font-size: 15px;
    font-weight: 500;
    color: var(--ink-gray);
    letter-spacing: 0.01em;
  }
  .site__dot {
    width: 18px;
    height: 18px;
    border-radius: 50%;
    background: var(--mark-white);
  }
</style>
</head>
<body>
  <main class="cover">
    <h1 class="title">
      <span class="title__strong">KINDLE</span>
      <span class="title__light">YOUR</span>
      <span class="title__strong">PATRONS</span>
    </h1>
    <p class="subtitle">Go to market with a story that <span class="subtitle__accent">SIZZLES</span></p>
    <div class="photo-field" role="img" aria-label="Rows of glossy white balls on a teal surface with a single red ball set apart from the group"></div>
    <div class="site">
      <span class="site__url">www.kindleyourpatrons.example</span>
      <span class="site__dot"></span>
    </div>
  </main>
</body>
</html>
```